Wine Label for White and Red Wine from California

We need a wine label for 2 whites and 2 red wines. (Merlot, Cabernet Sauvignon, Chardonnay, Pinot Grigio) Can be the same label or can have something to differentiate among them such as a color change. This is a label for an already existing wine on the US market but needs to be completely re-done. We want something way sharper, eye catching. Don't use the original label please as your starting point-- I don't think we want to see it anymore. But the structure of it is ok and the fonts are ok. (The tree is what is so awful about)

Target Market(s)

US market, always good to think of millennials, but still appeal to all ages. Men and women.

Colors

Designer to choose colors to be used in the design.

Requirements
Must have
• Should be eye catching, grabs attention, looks expensive, sells for a value price. Should feature the brand name and varietal and vintage:
• Dorvane Vineyards / Cabernet Sauvignon / 2014
• Bottle type is the 'Bordeaux Style' bottle. The white wine is a green bottle, the red wine uses a dark brown bottle. Be sure the labels look good on these bottles.
• What this bottle looks like is shown below.
• The label we are replacing is shown in the briefs.
Nice to have
• We feel successful labels have a lot of white background, stay away from dark labels-- they scratch too much when handled.
• Attached is a label we like, please look at the Cadenza label image below. But at the same time, we are flexible to your creativity. But nothing too crazy please.
Should not have
• Should not have a dark background.
• We are not big fans of grapes on the label unless extremely stylised. Nor do we like wine glasses, wine bottles.

```html
<!DOCTYPE html>
<html lang="en">
<head>
<meta charset="utf-8">
<title>Dorvane Vineyards – Wine Label Range</title>
<link rel="stylesheet" href="https://fonts.googleapis.com/css2?family=Cinzel:wght@400;500&family=Cormorant+Garamond:wght@500&display=swap">
<style>
  :root {
    --backdrop: #ececec;
    --paper: #f8f8f6;
    --paper-edge: #e2e2df;
    --ink: #1b1b1b;
    --red: #c0191b;
    --black: #1a1a1a;
    --vine-tone: #e6dcc6;
    --vine-fade: rgba(230, 220, 198, 0);
  }
  * { box-sizing: border-box; margin: 0; padding: 0; }
  html, body {
    width: 1029px;
    height: 1200px;
    overflow: hidden;
    background: var(--backdrop);
  }
  .range {
    position: relative;
    width: 1029px;
    height: 1200px;
  }
  .label {
    position: absolute;
    width: 343px;
    height: 514px;
    background: var(--paper);
    border: 1px solid var(--paper-edge);
    border-radius: 0 44px 0 44px;
    overflow: hidden;
    text-align: center;
    color: var(--ink);
  }
  .label--merlot     { left: 131px; top: 61px; }
  .label--cabernet   { left: 556px; top: 61px; }
  .label--chardonnay { left: 131px; top: 637px; }
  .label--pinot      { left: 556px; top: 637px; }

  .label--red   { --accent: var(--red); }
  .label--white { --accent: var(--black); }

  .brand-block {
    position: absolute;
    left: 70px;
    top: 0;
    width: 204px;
    height: 239px;
    background: var(--accent);
  }
  .vine-art {
    position: absolute;
    inset: 0;
    background:
      radial-gradient(ellipse 60% 30% at 55% 22%, var(--vine-tone), var(--vine-fade) 70%),
      radial-gradient(ellipse 60% 30% at 50% 62%, var(--vine-tone), var(--vine-fade) 70%),
      radial-gradient(ellipse 25% 12% at 38% 92%, var(--vine-tone), var(--vine-fade) 70%);
    opacity: 0.7;
  }

  .wordmark {
    position: absolute;
    left: 0;
    right: 0;
    font-family: "Cinzel", serif;
    font-weight: 500;
    color: var(--ink);
  }
  .wordmark__name {
    display: block;
    font-size: 44px;
    line-height: 1;
    letter-spacing: 0.01em;
  }
  .wordmark__sub {
    display: block;
    margin-top: 14px;
    font-size: 15px;
    line-height: 1;
    letter-spacing: 0.72em;
    padding-left: 0.72em;
  }
  .label--merlot .wordmark,
  .label--chardonnay .wordmark { top: 262px; }
  .label--cabernet .wordmark,
  .label--pinot .wordmark { top: 160px; }

  .tagline {
    position: absolute;
    left: 0;
    right: 0;
    top: 379px;
    font-family: "Cinzel", serif;
    font-size: 12.5px;
    line-height: 1;
    letter-spacing: 0.01em;
  }
  .varietal {
    position: absolute;
    left: 0;
    right: 0;
    top: 407px;
    height: 39px;
    background: var(--accent);
    color: #fff;
    font-family: "Cinzel", serif;
    font-size: 19px;
    line-height: 41px;
    letter-spacing: 0.03em;
  }
  .vintage {
    position: absolute;
    left: 0;
    right: 0;
    top: 458px;
    font-family: "Cormorant Garamond", serif;
    font-weight: 500;
    font-size: 30px;
    line-height: 1;
  }
</style>
</head>
<body>
<main class="range">

  <article class="label label--red label--merlot">
    <div class="brand-block"></div>
    <h2 class="wordmark"><span class="wordmark__name">DORVANE</span><span class="wordmark__sub">VINEYARDS</span></h2>
    <p class="tagline">QUALITY RED WINES SINCE 1996</p>
    <p class="varietal">MERLOT</p>
    <p class="vintage">2014</p>
  </article>

  <article class="label label--red label--cabernet">
    <div class="vine-art" role="img" aria-label="Faint line illustration of grape vines, leaves and bunches"></div>
    <h2 class="wordmark"><span class="wordmark__name">DORVANE</span><span class="wordmark__sub">VINEYARDS</span></h2>
    <p class="tagline">QUALITY RED WINES SINCE 1996</p>
    <p class="varietal">CABERNET SAUVIGNON</p>
    <p class="vintage">2014</p>
  </article>

  <article class="label label--white label--chardonnay">
    <div class="brand-block"></div>
    <h2 class="wordmark"><span class="wordmark__name">DORVANE</span><span class="wordmark__sub">VINEYARDS</span></h2>
    <p class="tagline">QUALITY WHITE WINES SINCE 1996</p>
    <p class="varietal">CHARDONNAY</p>
    <p class="vintage">2014</p>
  </article>

  <article class="label label--white label--pinot">
    <div class="vine-art" role="img" aria-label="Faint line illustration of grape vines, leaves and bunches"></div>
    <h2 class="wordmark"><span class="wordmark__name">DORVANE</span><span class="wordmark__sub">VINEYARDS</span></h2>
    <p class="tagline">QUALITY WHITE WINES SINCE 1996</p>
    <p class="varietal">PINOT GRIGIO</p>
    <p class="vintage">2014</p>
  </article>

</main>
</body>
</html>
```